Vitamin B12 Liquid Drops Label

hi, i need a label designed for my vitamin b12 drops that i am going to be selling on bazaroo. the label needs to quickly capture the attention of a buyer as he or she is scrolling through the thumbnail search results on bazaroo.example my brand is called zulpa. i already have an example brand logo i will be using, however, i need help designing the rest of the label. attached are some examples of labels i like for other supplements.some of these examples are pink. i do not want pink. please go for a blue/green color scheme. THE DESIGN MUST BE BOLD

Target Market(s)

adults ages 30 - 64

Font styles to use
Sans Serif

Colors
0455a3
cedeed
3176b5
85acd3
cfdeed
9bcb3b
abd037
cadf82
00a990

Requirements
Must have
• - bold design
• - somewhat gender-neutral color scheme because this will be used equally by men and women
• - B12 MUST be very prominent and visible on the label
Should not have
• - it should not be "crunchy" looking

```html
<!DOCTYPE html>
<html lang="en">
<head>
<meta charset="utf-8">
<title>Zulpa B12 Drops Label</title>
<link href="https://fonts.googleapis.com/css2?family=Mulish:wght@400;600;700;900&family=Zilla+Slab:wght@700&display=swap" rel="stylesheet">
<style>
  :root {
    --label-bg: #e6e7e8;
    --page-bg: #ffffff;
    --teal: #16a89a;
    --plum: #2e1c4a;
    --plum-soft: #3f2a5e;
    --ink: #1b1b22;
    --white: #ffffff;
  }
  * { box-sizing: border-box; margin: 0; padding: 0; }
  html, body { width: 1200px; height: 1000px; overflow: hidden; background: var(--page-bg); }
  body { font-family: "Mulish", Arial, sans-serif; position: relative; }

  .label { position: absolute; left: 91px; top: 58px; width: 1021px; height: 462px; background: var(--label-bg); overflow: hidden; }
  .pattern-strip { position: absolute; background: linear-gradient(180deg, var(--teal), #0f9487); }
  .pattern-strip--left { left: 0; top: 0; width: 44px; height: 462px; }
  .pattern-strip--right { left: 594px; top: 177px; width: 63px; height: 285px; }

  /* left panel */
  .nutrition { position: absolute; left: 96px; top: 34px; width: 150px; }
  .nutrition__title { color: var(--teal); font-weight: 600; font-size: 17px; padding-bottom: 6px; border-bottom: 4px solid var(--teal); }
  .nutrition__table { margin-top: 12px; border: 3px solid var(--teal); }
  .nutrition__row { color: var(--teal); font-weight: 700; font-size: 11.5px; line-height: 12px; padding: 5px 7px 4px; }
  .nutrition__row + .nutrition__row { border-top: 3px solid var(--teal); }
  .warning { position: absolute; left: 102px; top: 253px; width: 180px; color: var(--teal); }
  .warning__head { display: flex; align-items: center; gap: 6px; font-size: 12px; font-weight: 600; letter-spacing: .3px; margin-bottom: 4px; }
  .warning__text { font-size: 13px; line-height: 16.5px; }

  /* centre panel */
  .brand-band { position: absolute; left: 360px; top: 0; width: 285px; height: 89px; background: var(--plum); display: flex; align-items: center; justify-content: center; }
  .brand-name { color: var(--white); font-weight: 900; font-size: 56px; letter-spacing: 1px; }
  .product-name { position: absolute; left: 361px; top: 100px; font-family: "Zilla Slab", Georgia, serif; font-weight: 700; color: var(--plum); font-size: 80px; line-height: 1; letter-spacing: 2px; }
  .product-form { position: absolute; left: 363px; top: 178px; font-family: "Zilla Slab", Georgia, serif; font-weight: 700; color: var(--plum); font-size: 25px; letter-spacing: 1px; }
  .rule { position: absolute; left: 360px; width: 255px; height: 1px; background: #d4d4d8; }
  .drop { position: absolute; left: 420px; top: 238px; }
  .volume { position: absolute; left: 361px; top: 422px; width: 248px; height: 42px; background: var(--plum); border-radius: 10px 10px 0 0; color: var(--white); font-size: 19px; font-weight: 400; display: flex; align-items: center; justify-content: center; }

  /* right panel */
  .info { position: absolute; left: 714px; width: 237px; }
  .info__title { color: var(--ink); font-weight: 600; font-size: 17.5px; margin-bottom: 6px; }
  .info__text { color: var(--teal); font-size: 13px; line-height: 16.5px; text-align: justify; }
  .company { position: absolute; left: 714px; top: 305px; color: var(--ink); font-size: 15px; line-height: 19px; }
  .batch { position: absolute; left: 841px; top: 358px; width: 110px; height: 47px; border: 2px solid var(--ink); color: var(--ink); font-size: 13px; line-height: 16px; padding: 4px 8px; }
</style>
</head>
<body>
  <section class="label">
    <div class="pattern-strip pattern-strip--left" role="img" aria-label="Teal leaf braid decorative pattern"></div>

    <div class="nutrition">
      <h2 class="nutrition__title">Nutrition Facts</h2>
      <div class="nutrition__table">
        <p class="nutrition__row">Lorem ipsum<br>Lorem ipsum<br>Lorem ipsum</p>
        <p class="nutrition__row">Lorem ipsum</p>
        <p class="nutrition__row">Lorem ipsum<br>Lorem ipsum<br>Lorem ipsum<br>Lorem ipsum</p>
      </div>
    </div>

    <div class="warning">
      <p class="warning__head">WARNING
        <svg width="18" height="16" viewBox="0 0 18 16" aria-hidden="true"><path d="M9 1 L17 15 H1 Z" fill="#16a89a" stroke="#16a89a" stroke-linejoin="round" stroke-width="2"/><rect x="8.2" y="6" width="1.6" height="5" fill="#fff"/><rect x="8.2" y="12" width="1.6" height="1.6" fill="#fff"/></svg>
      </p>
      <p class="warning__text">Lorem ipsum dolor sit amet, consectetuer adipiscing elit, sed diam nonummy nibh euismod tincidunt ut laoreet dolore</p>
    </div>

    <div class="brand-band"><span class="brand-name">ZULPA</span></div>
    <div class="rule" style="top:140px"></div>
    <h1 class="product-name">B12</h1>
    <p class="product-form">drops</p>
    <div class="rule" style="top:206px"></div>
    <svg class="drop" width="120" height="170" viewBox="0 0 120 170" aria-hidden="true">
      <path d="M60 2 C72 40 112 78 112 114 A52 52 0 0 1 8 114 C8 78 48 40 60 2 Z" fill="#3f2a5e"/>
    </svg>
    <div class="volume">2 FL OZ (60ml)</div>

    <div class="pattern-strip pattern-strip--right" role="img" aria-label="Teal leaf braid decorative pattern"></div>

    <div class="info" style="top:43px">
      <h3 class="info__title">Ingredient</h3>
      <p class="info__text">Lorem ipsum dolor sit amet, consectetuer adipiscing elit, sed diam nonummy nibh euismod tincidunt ut laoreet</p>
    </div>
    <div class="info" style="top:153px">
      <h3 class="info__title">Recommendation</h3>
      <p class="info__text">Lorem ipsum dolor sit amet, consectetuer adipiscing elit, sed diam nonummy nibh euismod tincidunt ut laoreet</p>
    </div>

    <p class="company">Company Address<br>Made in Switzerland</p>
    <div class="batch">Batch:<br>Expiry Date:</div>
  </section>
</body>
</html>
```